Skatepark, and Teenage Music/Recreation Venue needs logo, business card and letterhead. Website desi

- Logo, Letterhead & Business Card design for a new start Skatepark and Youth Venue called "The Orbit" (Pty.Ltd company) in Australia.

- Website and App design will follow within 6-months.

- Facility centered around world class skatepark which incorporates the use of innovative technology applications to enhance consumer experience, it will also provide a live entertainment & music venue for teenagers.

- Appearance should appeal to the 'mature' teenage population, the aim is provide an excellent membership experience which can be associated with the club brand.

Overall the design should communicate:
Excitement, energy, exclusivity and style

- Clean and modern fonts and styling preferred.
- Logos the I personally like: Brinmore, Quellstone, (but they don't have to be round!)
- Generally I prefer understated business cards that are subtlety/elegently distinct
- ideally the logo would be expected to standalone if no text were available. (if that makes sense?)

Business

The Orbit

```html
<!DOCTYPE html>
<html lang="en">
<head>
<meta charset="utf-8">
<title>The Orbit — Stationery</title>
<link rel="stylesheet" href="https://fonts.googleapis.com/css2?family=Source+Sans+3:wght@400;600&display=swap">
<style>
  :root {
    --bg: #ececed;
    --paper: #ffffff;
    --navy: #15222b;
    --blue: #2f8fdd;
    --blue-faint: #dde9f4;
    --ink: #2b2f33;
    --ink-soft: #6b7075;
  }
  * { box-sizing: border-box; margin: 0; padding: 0; }
  html, body { width: 1200px; height: 795px; overflow: hidden; }
  body {
    background: var(--bg);
    font-family: "Source Sans 3", "Helvetica Neue", Arial, sans-serif;
    color: var(--ink);
    position: relative;
  }

  /* Shared brand lockup */
  .brand {
    display: flex; align-items: center; gap: 7px;
    font-weight: 600; white-space: nowrap;
  }
  .brand .dot {
    width: 14px; height: 14px; border-radius: 50%;
    background: var(--blue); flex: none;
  }

  /* Letterhead */
  .letterhead {
    position: absolute; left: 640px; top: 44px;
    width: 500px; height: 707px;
    background: var(--paper);
    box-shadow: 0 6px 18px rgba(0,0,0,.12);
    overflow: hidden;
  }
  .letterhead .faint-motif {
    position: absolute; left: 200px; top: 0;
    width: 300px; height: 330px;
    background: radial-gradient(ellipse at 100% 0%, var(--blue-faint) 0%, rgba(221,233,244,.5) 45%, rgba(255,255,255,0) 75%);
  }
  .letterhead .edge-motif {
    position: absolute; right: 0; top: 44px;
    width: 60px; height: 286px;
    background: linear-gradient(180deg, var(--blue) 0%, #24577f 50%, var(--navy) 100%);
  }
  .letterhead .header-bar {
    position: absolute; right: 0; top: 0;
    width: 170px; height: 44px;
    background: var(--navy);
    display: flex; align-items: center; justify-content: flex-end;
    padding-right: 18px;
  }
  .letterhead .brand { color: #fff; font-size: 17px; }
  .letter-body {
    position: absolute; left: 44px; top: 92px; width: 350px;
    font-size: 9.5px; line-height: 1.45; color: var(--ink);
  }
  .letter-body p { margin-bottom: 10px; }
  .letter-body .salutation { margin-bottom: 12px; }
  .letter-foot {
    position: absolute; left: 44px; bottom: 28px;
    font-size: 8px; color: var(--ink-soft); letter-spacing: .2px;
  }

  /* Business cards */
  .card {
    position: absolute; left: 110px;
    width: 340px; height: 195px;
    overflow: hidden;
    box-shadow: 0 5px 14px rgba(0,0,0,.15);
  }
  .card .motif { position: absolute; inset: 0; }
  .card-front { top: 200px; }
  .card-front .motif {
    background: radial-gradient(ellipse at 50% 50%, var(--navy) 0%, var(--navy) 45%, #1f4a6d 75%, var(--blue) 100%);
  }
  .card-back { top: 450px; background: var(--paper); }
  .card-back .motif {
    background: radial-gradient(ellipse at 50% 50%, var(--paper) 0%, var(--paper) 60%, #b9d7f1 85%, var(--blue) 110%);
  }
  .card .brand {
    position: absolute; left: 0; right: 0;
    justify-content: center;
  }
  .card-front .brand { top: 84px; color: #fff; font-size: 22px; }
  .card-back .brand { top: 34px; color: var(--navy); font-size: 18px; }
  .card-back .contact {
    position: absolute; left: 0; right: 0; top: 70px;
    text-align: center; font-size: 8px; line-height: 1.5; color: var(--ink-soft);
  }
  .contact .name { font-size: 13px; font-weight: 600; color: var(--navy); }
  .contact .role { font-size: 8.5px; margin-bottom: 5px; }
</style>
</head>
<body>

  <section class="letterhead" aria-label="Letterhead">
    <div class="faint-motif" role="img" aria-label="Faint blue decorative pattern area"></div>
    <div class="edge-motif" role="img" aria-label="Blue and navy decorative pattern strip"></div>
    <div class="header-bar">
      <div class="brand"><span class="dot"></span>The Orbit</div>
    </div>

    <div class="letter-body">
      <p class="salutation">Dear member,</p>
      <p>Thank you for joining our crew this season. Your pass opens the bowl, the street course and every live night in the hall, seven days a week from early till late.</p>
      <p>Each session is tracked in our app, so you can log tricks, book coaching and see what is on stage before you arrive. Lockers, repairs and a quiet study lounge are free for members.</p>
      <p>We ask every rider to wear a helmet, respect the queue and look out for younger skaters. Our staff are always close by if you need a hand.</p>
    </div>

    <div class="letter-foot">418 Kestrel Lane, Ashford, NSW 2361 &nbsp;Ph: 555-014-7780 / 555-014-7781 &nbsp;hi@yoursite.com · www.yoursite.com</div>
  </section>

  <section class="card card-front" aria-label="Business card front">
    <div class="motif" role="img" aria-label="Navy card face with blue decorative pattern toward the edges"></div>
    <div class="brand"><span class="dot"></span>The Orbit</div>
  </section>

  <section class="card card-back" aria-label="Business card back">
    <div class="motif" role="img" aria-label="White card face with blue decorative pattern toward the edges"></div>
    <div class="brand"><span class="dot"></span>The Orbit</div>
    <div class="contact">
      <div class="name">John Doe</div>
      <div class="role">Manager</div>
      <div>418 Kestrel Lane, Ashford, NSW 2361</div>
      <div>555-014-7780 | hi@yoursite.com</div>
      <div>www.yoursite.com</div>
    </div>
  </section>

</body>
</html>
```